One of Australia's fastest growing energy maintenance contractors needs a new website

www.panelbrite.com.au
Our business has evolved over the past years and now our website is no longer relevant.
We clean solar panels and we vacuum roof gutters.
We clean solar panels on the roofs of residential houses right up to billion dollar solar farms with in excess of 1 million panels. We offer thermal image testing and bird proofing for our residential and commercial clients and thermal drone imaging services for our solar farm clients.
We vacuum clean roof gutters (using a LoftSuk) on the residential house next door right up to enormous private and public schools, colleges, shopping centres, strat complexes and commercial buildings.
When first built our business had more of a domestic residential skew and the website reflected that. While that is still part of our core business we are now bidding on and have secured large government, commercial and infrastructure contracts and our new website needs to reflect our growth and our new business. We need a new site that it optimised for both desktop ad phone viewing as our latest figures showed that 73% of people visiting our site are on mobile phones. We have an extensive amount of data on Trekmetrics available as well as Bidlinks. Both that would also need integrating with the site along with a few other plugins such as Kembo Chat IQ, Friendwall etc along with SEO key words etc. We are also the winner and finalists over multiple years of the small business of the year awards and we like to proudly and prominently display those on our site.
We are looking for a new site with a modern professional feel / theme
There is a definitive break in our business between the solar Panel cleaning clients and the gutter cleaning clients so we would like a home page that begins with a simple choice:
Solar Panel Cleaning – Gutter Cleaning
With a professional full screen background image (we have hundreds to choose from) and along the bottom a small area with rights reserved etc, phone number etc (at some point in the future we will split these into two businesses but for now it’s what we have).
After that selection is made we would like a repeat of that same scenario but the selection is:
If it’s Solar Panel Cleaning
(new background image)
Government – Infrastructure – Commercial – Residential
If it’s Gutter Cleaning
(new background image)
Government – Strata – Commercial – Residential
After making those choices then onto the relevant pages with background images relevant to each sector and a them that suits (on the residential we would like to keep the link to our trekmetrics reviews) - We will provide copy / text for each relevant page.
Other than that, a menu inclusive of the above and:
Resellers Portal – we will provide a link to this from Kembo CRM)
Customer portal (we will supply a link to this from our booking system)
We also need a page for our Solar Resellers / Partners page but we will give them a link to this, it won’t be listed on the site.
Request a quote page (Again we will provide information from Kembo as this will be linked to the CRM)
Standard contact us page inclusive of phone numbers, address and fields supplied from CRM
Sydney – 02 7391 5084
Southern Highlands – 02 4863 1507
Goulburn – 02 4863 1507
Canberra – 02 6178 3045
Wollongong – 02 4239 7615
sales@panelbrite.com.au
Head Office - Ferndell NSW 2583
ABN: 48762093115
Responsive Design: Optimized for desktop and mobile (73% mobile visitors).
Fast Loading Speed: Optimized for performance.
Smooth Transition Animations: For service and category selection.
Sticky Contact Bar: Always accessible at the bottom of mobile screens for quick calls.
SEO Optimization: Focused on government tenders, large-scale commercial contracts, and infrastructure projects.
Integrations
Trekmetrics & Trekmetrics Bidlinks.
Kembo Chat IQ.
Friendwall Beacon.
SEO tools and keyword optimization.
Many many more images available if needed

```html
<!DOCTYPE html>
<html lang="en">
<head>
<meta charset="utf-8">
<title>PanelBrite – Solar Cleaning &amp; Vacuum Roof Gutters Cleaning</title>
<link rel="stylesheet" href="https://fonts.googleapis.com/css2?family=Outfit:wght@300;400;500;600;700&display=swap">
<style>
:root{
  --navy:#0b3a6e;
  --blue-dark:#0d4f94;
  --blue:#1f86d3;
  --blue-light:#2ea6e0;
  --sky:#dbe8f4;
  --ink:#333f4d;
  --gold:#f2b01e;
  --white:#ffffff;
}
*{box-sizing:border-box;margin:0;padding:0}
html,body{width:1200px;height:4013px;overflow:hidden;background:var(--white);font-family:'Outfit',sans-serif;color:var(--ink)}
.page{position:relative;width:1200px;height:4013px;overflow:hidden}
.abs{position:absolute}
.center{left:0;width:1200px;text-align:center}

/* header */
.site-header{position:absolute;top:0;left:0;width:1200px;height:78px;background:var(--white);z-index:5}
.brand{position:absolute;left:106px;top:20px;display:flex;align-items:center;gap:12px}
.brand-square{width:38px;height:38px;background:var(--blue)}
.brand-name{font-size:27px;font-weight:500;color:var(--blue-dark)}
.main-nav{position:absolute;left:373px;top:32px;display:flex;gap:26px;font-size:14px;color:#3a4a5c}
.header-cta{position:absolute;right:0;top:0;width:210px;height:78px;background:var(--blue-dark);color:var(--white);font-weight:600;font-size:15px;display:flex;align-items:center;justify-content:center;clip-path:polygon(10% 0,100% 0,100% 100%,0 100%)}

/* hero */
.hero-photo{position:absolute;top:78px;left:0;width:1200px;height:640px;background:linear-gradient(180deg,#cfe1f2 0%,#e9f1f8 45%,#8fb3d5 80%,#4b79a8 100%)}
.hero-badge{position:absolute;top:142px;left:465px;width:290px;height:24px;background:var(--navy);color:var(--white);font-size:15px;font-weight:600;letter-spacing:1.5px;display:flex;align-items:center;justify-content:center;clip-path:polygon(3% 0,100% 0,97% 100%,0 100%)}
.hero-title{position:absolute;top:172px;font-size:46px;font-weight:600;line-height:50px}
.hero-title .l1{color:var(--blue-dark)}
.hero-title .l2{color:var(--blue)}
.hero-sub{position:absolute;top:284px;font-size:15px;color:#2c3a48}
.btn{display:flex;align-items:center;justify-content:center;gap:8px;background:var(--blue);color:var(--white);font-weight:600;font-size:15px}
.hero-btn{position:absolute;top:322px;left:517px;width:192px;height:49px}
.btn-tab{width:26px;height:49px;background:var(--blue-dark);position:absolute;left:0;top:0}
.scroll-dot{position:absolute;top:578px;left:578px;width:44px;height:44px;border-radius:50%;background:rgba(255,255,255,.45);display:flex;align-items:center;justify-content:center}

/* service choice */
.choice{position:absolute;top:0;left:0;width:1200px;height:1260px;pointer-events:none}
.choice-item{position:absolute;top:776px;width:600px;text-align:center;color:var(--white)}
.choice-icon{width:100px;height:100px;border-radius:50%;margin:0 auto;background:var(--navy);border:3px solid var(--blue-light);display:flex;align-items:center;justify-content:center}
.choice-item.right .choice-icon{background:var(--blue);border-color:#7cc6ee}
.choice-item h2{font-size:27px;font-weight:600;margin-top:30px;letter-spacing:.3px}
.choice-item p{font-size:15px;line-height:19px;margin:10px auto 0;width:330px}
.choice-item svg.chev{margin-top:10px}

/* section headings */
.section-title{position:absolute;font-size:42px;font-weight:600;color:var(--blue-dark)}
.section-sub{position:absolute;font-size:16px;color:var(--blue-dark)}
.on-blue{color:var(--white)}

/* hexagons */
.hex{position:absolute;top:1382px;width:262px;height:302px}
.hex-label{position:absolute;left:0;width:262px;top:208px;text-align:center;color:var(--white);font-size:25px;font-weight:600}

/* gutter band */
.gutter-card{position:absolute;top:2046px;height:291px;overflow:hidden}
.gutter-card .label{position:absolute;left:27px;bottom:20px;color:var(--white);font-size:24px;font-weight:600}
.gutter-card.feature{top:2025px;height:331px;background:var(--navy);color:var(--white);padding:75px 38px 0 38px}
.feature h3{font-size:24px;font-weight:600}
.feature p{font-size:13px;line-height:18px;margin-top:10px}
.feature .more{display:inline-block;margin-top:16px;font-size:12px;border-bottom:1px solid var(--white);letter-spacing:.5px}

/* testimonials */
.review{position:absolute;top:2524px;width:295px;height:265px;background:var(--white);border:1px solid #e3e8ee;box-shadow:0 4px 14px rgba(0,40,90,.07);padding:28px 37px 0 37px}
.review.active{background:var(--blue-dark);border-color:var(--blue-dark);color:var(--white)}
.review .quote{font-size:40px;line-height:30px;color:var(--blue);font-weight:700;font-family:Georgia,serif}
.review.active .quote{color:#7cc6ee}
.review p{font-size:11.5px;line-height:20px;margin-top:6px}
.review .stars{color:var(--gold);font-size:18px;letter-spacing:1px;margin-top:8px}
.review .by{font-size:13px;font-weight:600;margin-top:6px}
.arrow-btn{position:absolute;top:2636px;width:46px;height:46px;border-radius:50%;background:var(--white);box-shadow:0 3px 12px rgba(0,40,90,.15);display:flex;align-items:center;justify-content:center}

/* quote form */
.house-photo{position:absolute;top:3300px;left:0;width:1200px;height:327px;background:linear-gradient(180deg,#e8eef4 0%,#7a93b0 40%,#3e5f86 70%,#7b5f4e 100%)}
.quote-box{position:absolute;top:2848px;left:143px;width:935px;height:536px;background:linear-gradient(135deg,var(--blue-dark) 0%,var(--blue) 55%,var(--blue-light) 100%);border-radius:94px 0 94px 0}
.field{position:absolute;height:54px;background:var(--white);border:1px solid #c8d6e4;display:flex;align-items:center;gap:12px;padding-left:20px;font-size:15px;color:#3a4350}
.field.area{align-items:flex-start;padding-top:16px}
.send-btn{position:absolute;top:3272px;left:513px;width:207px;height:51px;background:var(--blue-dark)}
.send-btn .btn-tab{height:51px;background:var(--white);width:22px;clip-path:polygon(0 0,100% 20%,100% 80%,0 100%)}

/* footer */
.site-footer{position:absolute;top:3627px;left:0;width:1200px;height:330px;background:var(--blue-dark);color:var(--white)}
.footer-bar{position:absolute;top:3957px;left:0;width:1200px;height:56px;background:#1865b3;color:var(--white);font-size:13px;display:flex;align-items:center;justify-content:center}
.foot-brand{position:absolute;left:105px;top:70px;width:220px;text-align:center}
.foot-mark{width:62px;height:62px;border-radius:50%;background:var(--white);margin:0 auto}
.foot-name{font-size:31px;font-weight:500;margin-top:36px}
.socials{display:flex;justify-content:center;gap:8px;margin-top:14px}
.socials span{width:27px;height:27px;border-radius:50%;border:2px solid var(--white)}
.foot-col{position:absolute;top:82px}
.foot-col h4{font-size:18px;font-weight:600;letter-spacing:1.5px;padding-bottom:10px;border-bottom:1px solid rgba(255,255,255,.35);display:inline-block}
.foot-col ul{list-style:none;margin-top:14px;font-size:14px;line-height:22.6px}
.foot-col li{display:flex;align-items:center;gap:7px}
</style>
</head>
<body>
<div class="page">

  <header class="site-header">
    <div class="brand"><span class="brand-square"></span><span class="brand-name">PanelBrite</span></div>
    <nav class="main-nav">
      <span>Solar Cleaning</span><span>Gutter Cleaning</span><span>Resellers Portal</span><span>Customer portal</span><span>Contact Us</span>
    </nav>
    <div class="header-cta">Request a Quote &nbsp;›</div>
  </header>

  <div class="hero-photo" role="img" aria-label="Two workers cleaning solar panels and pressure-washing a tiled roof under a bright sky"></div>
  <div class="hero-badge">WELCOME TO PANELBRITE</div>
  <h1 class="hero-title center"><span class="l1">Solar Cleaning &amp; Vacuum</span><br><span class="l2">Roof Gutters Cleaning</span></h1>
  <p class="hero-sub center">We have a detailed knowledge of the cleaning &amp; testing of Solar Panels</p>
  <div class="btn hero-btn"><span class="btn-tab"></span><span style="margin-left:26px">GET A QUOTE &nbsp;›</span></div>
  <div class="scroll-dot"><svg width="20" height="22" viewBox="0 0 20 22"><path d="M10 1V20M3 13l7 7 7-7" stroke="#1f86d3" stroke-width="2" fill="none"/></svg></div>

  <svg class="choice" width="1200" height="1260" viewBox="0 0 1200 1260" aria-hidden="true">
    <defs>
      <linearGradient id="gLeft" x1="0" y1="0" x2="0" y2="1"><stop offset="0" stop-color="#2b95dc"/><stop offset="1" stop-color="#1d7fd0"/></linearGradient>
      <linearGradient id="gRight" x1="0" y1="0" x2="0" y2="1"><stop offset="0" stop-color="#0c4f93"/><stop offset="1" stop-color="#0e5aa3"/></linearGradient>
    </defs>
    <polygon points="0,640 612,701 612,1142 0,1215" fill="url(#gLeft)"/>
    <polygon points="612,701 1200,631 1200,1212 612,1142" fill="url(#gRight)"/>
    <line x1="613" y1="701" x2="613" y2="1246" stroke="#9fb8cf" stroke-width="1"/>
  </svg>

  <div class="choice-item" style="left:20px">
    <div class="choice-icon"><svg width="50" height="50" viewBox="0 0 50 50" fill="none" stroke="#fff" stroke-width="2"><path d="M10 10h30l5 20H5z"/><path d="M17 10l-3 20M25 10v20M33 10l3 20M8 20h34"/><path d="M25 30v10M17 42h16"/></svg></div>
    <h2>SOLAR PANEL CLEANING</h2>
    <p>Lorem ipsum dolor sit amet consectetur adipiscing elit sed do eiusmod</p>
    <svg class="chev" width="26" height="16" viewBox="0 0 26 16"><path d="M2 3l11 10L24 3" stroke="#fff" stroke-width="2.5" fill="none"/></svg>
  </div>
  <div class="choice-item right" style="left:615px">
    <div class="choice-icon"><svg width="56" height="40" viewBox="0 0 56 40" fill="none" stroke="#fff" stroke-width="2"><path d="M2 30h52M6 30l6-18h38l-4 18M14 12v18M22 12v18M30 12v18M38 12v18"/><path d="M40 12l8-10"/></svg></div>
    <h2>ROOF GUTTER CLEANING</h2>
    <p>Lorem ipsum dolor sit amet consectetur adipiscing elit sed do eiusmod</p>
    <svg class="chev" width="26" height="16" viewBox="0 0 26 16"><path d="M2 3l11 10L24 3" stroke="#fff" stroke-width="2.5" fill="none"/></svg>
  </div>

  <!-- solar panel sectors -->
  <h2 class="section-title center" style="top:1260px">Solar Panel Cleaning</h2>
  <p class="section-sub center" style="top:1330px">Lorem ipsum dolor sit amet, consectetur adipiscing elit, sed do eiusmod tempor incid</p>

  <div class="hex" style="left:54px">
    <svg width="262" height="302" viewBox="0 0 262 302" role="img" aria-label="Rooftop solar array on a government building"><defs><linearGradient id="h1" x1="0" y1="0" x2="0" y2="1"><stop offset="0" stop-color="#b8c7d3"/><stop offset=".5" stop-color="#8a6f5a"/><stop offset="1" stop-color="#2d4766"/></linearGradient></defs><polygon points="131,1 261,76 261,226 131,301 1,226 1,76" fill="url(#h1)"/><polygon points="131,14 250,83 250,219 131,288 12,219 12,83" fill="none" stroke="#fff" stroke-opacity=".5"/></svg>
    <div class="hex-label">Government</div>
  </div>
  <div class="hex" style="left:335px">
    <svg width="262" height="302" viewBox="0 0 262 302" role="img" aria-label="Large solar farm with transmission towers"><defs><linearGradient id="h2" x1="0" y1="0" x2="0" y2="1"><stop offset="0" stop-color="#8fb4d6"/><stop offset=".5" stop-color="#3f6a98"/><stop offset="1" stop-color="#13335a"/></linearGradient></defs><polygon points="131,1 261,76 261,226 131,301 1,226 1,76" fill="url(#h2)"/><polygon points="131,14 250,83 250,219 131,288 12,219 12,83" fill="none" stroke="#fff" stroke-opacity=".5"/></svg>
    <div class="hex-label">Infrastructure</div>
  </div>
  <div class="hex" style="left:616px">
    <svg width="262" height="302" viewBox="0 0 262 302" role="img" aria-label="Solar carport canopy over parked cars"><defs><linearGradient id="h3" x1="0" y1="0" x2="0" y2="1"><stop offset="0" stop-color="#9cc4e8"/><stop offset=".45" stop-color="#3d82c8"/><stop offset="1" stop-color="#1d2f48"/></linearGradient></defs><polygon points="131,1 261,76 261,226 131,301 1,226 1,76" fill="url(#h3)"/><polygon points="131,14 250,83 250,219 131,288 12,219 12,83" fill="none" stroke="#fff" stroke-opacity=".5"/></svg>
    <div class="hex-label">Commercial</div>
  </div>
  <div class="hex" style="left:897px">
    <svg width="262" height="302" viewBox="0 0 262 302" role="img" aria-label="Residential house with solar panels on a tiled roof"><defs><linearGradient id="h4" x1="0" y1="0" x2="0" y2="1"><stop offset="0" stop-color="#a7c6e6"/><stop offset=".45" stop-color="#6b4638"/><stop offset="1" stop-color="#263c55"/></linearGradient></defs><polygon points="131,1 261,76 261,226 131,301 1,226 1,76" fill="url(#h4)"/><polygon points="131,14 250,83 250,219 131,288 12,219 12,83" fill="none" stroke="#fff" stroke-opacity=".5"/></svg>
    <div class="hex-label">Residential</div>
  </div>

  <!-- gutter band -->
  <svg class="abs" style="left:0;top:1695px" width="1200" height="567" viewBox="0 0 1200 567" role="img" aria-label="Blue tinted background of a building roof">
    <defs><linearGradient id="gBand" x1="0" y1="0" x2="0" y2="1"><stop offset="0" stop-color="#1d7fd0"/><stop offset="1" stop-color="#0f5aa6"/></linearGradient></defs>
    <polygon points="0,0 600,120 1200,0 1200,567 0,567" fill="url(#gBand)"/>
    <line x1="600" y1="65" x2="600" y2="120" stroke="#cfe0ef" stroke-width="1"/>
  </svg>
  <h2 class="section-title center on-blue" style="top:1890px">Gutter Cleaning</h2>
  <p class="section-sub center on-blue" style="top:1955px;font-size:17px">Lorem ipsum dolor sit amet, consectetur adipiscing elit sed do eiusmod incid</p>

  <div class="gutter-card" style="left:75px;width:265px;background:linear-gradient(180deg,#6d9bd0 0%,#a9c3de 40%,#3e5369 100%)" role="img" aria-label="Government office building with a communications tower"><span class="label">Government</span></div>
  <div class="gutter-card feature" style="left:340px;width:265px">
    <h3>Strata</h3>
    <p>Lorem ipsum dolor sit amet, consectetur adipiscing elit, sed do eiusmod tempor incididunt ut labore et dolore magna aliqua. Quis ipsum suspendisse ultrices gravida Risus</p>
    <span class="more">LEARN MORE &nbsp;›</span>
  </div>
  <div class="gutter-card" style="left:605px;width:264px;background:linear-gradient(180deg,#c9a531 0%,#6f7a5a 30%,#4a5563 60%,#2e3947 100%)" role="img" aria-label="Flat commercial roof with skylights"><span class="label">Commercial</span></div>
  <div class="gutter-card" style="left:869px;width:268px;background:linear-gradient(180deg,#c7d3df 0%,#7d8895 45%,#5b636d 100%)" role="img" aria-label="Residential house roof with a gable window"><span class="label">Residential</span></div>

  <!-- testimonials -->
  <h2 class="section-title center" style="top:2420px">What People Says</h2>

  <div class="arrow-btn" style="left:64px"><svg width="20" height="14" viewBox="0 0 20 14"><path d="M19 7H2M8 1L2 7l6 6" stroke="#1f86d3" stroke-width="2" fill="none"/></svg></div>
  <div class="arrow-btn" style="left:1102px"><svg width="20" height="14" viewBox="0 0 20 14"><path d="M1 7h17M12 1l6 6-6 6" stroke="#1f86d3" stroke-width="2" fill="none"/></svg></div>

  <div class="review" style="left:156px">
    <div class="quote">“</div>
    <p>"Lorem ipsum dolor sit amet, consecte-tur adipiscing elit, sed do eiusmod tempor incididunt ut labore et dolore magna aliqua. Ut enim ad minim veniam, quis nostrud exercitation ullam-co laboris nisi ut aliquip ex ea c</p>
    <div class="stars">★★★★★</div>
    <div class="by">By Author name</div>
  </div>
  <div class="review active" style="left:467px">
    <div class="quote">“</div>
    <p>"Lorem ipsum dolor sit amet, consecte-tur adipiscing elit, sed do eiusmod tempor incididunt ut labore et dolore magna aliqua. Ut enim ad minim veniam, quis nostrud exercitation ullam-co laboris nisi ut aliquip ex ea c</p>
    <div class="stars">★★★★★</div>
    <div class="by">By Author name</div>
  </div>
  <div class="review" style="left:776px">
    <div class="quote">“</div>
    <p>"Lorem ipsum dolor sit amet, consecte-tur adipiscing elit, sed do eiusmod tempor incididunt ut labore et dolore magna aliqua. Ut enim ad minim veniam, quis nostrud exercitation ullam-co laboris nisi ut aliquip ex ea c</p>
    <div class="stars">★★★★★</div>
    <div class="by">By Author name</div>
  </div>

  <!-- quote form -->
  <div class="house-photo" role="img" aria-label="House with rows of solar panels on a tiled roof"></div>
  <div class="quote-box"></div>
  <h2 class="section-title center on-blue" style="top:2908px;font-size:38px">Request a Quote</h2>

  <div class="field" style="left:238px;top:2988px;width:370px"><svg width="18" height="18" viewBox="0 0 18 18" fill="none" stroke="#8a96a3" stroke-width="1.4"><circle cx="9" cy="6" r="4"/><path d="M2 17c0-4 3-6 7-6s7 2 7 6"/></svg>First Name*</div>
  <div class="field" style="left:618px;top:2988px;width:365px"><svg width="18" height="18" viewBox="0 0 18 18" fill="none" stroke="#8a96a3" stroke-width="1.4"><circle cx="9" cy="6" r="4"/><path d="M2 17c0-4 3-6 7-6s7 2 7 6"/></svg>Last Name*</div>
  <div class="field" style="left:238px;top:3057px;width:370px"><svg width="20" height="14" viewBox="0 0 20 14" fill="none" stroke="#8a96a3" stroke-width="1.4"><rect x="1" y="1" width="18" height="12"/><path d="M1 1l9 7 9-7"/></svg>E-mail*</div>
  <div class="field" style="left:618px;top:3057px;width:370px"><svg width="18" height="18" viewBox="0 0 18 18" fill="none" stroke="#8a96a3" stroke-width="1.4"><path d="M4 1l3 4-2 2c1 2 4 5 6 6l2-2 4 3-2 3C8 17 1 10 1 3z"/></svg>Phone number*</div>
  <div class="field area" style="left:240px;top:3124px;width:748px;height:121px"><svg width="22" height="20" viewBox="0 0 22 20" fill="none" stroke="#8a96a3" stroke-width="1.4"><path d="M11 1C5 1 1 4.5 1 9c0 2 1 4 3 5l-1 5 5-3c1 .3 2 .4 3 .4 6 0 10-3.5 10-7.9S17 1 11 1z"/></svg>Leave Message</div>
  <div class="btn send-btn"><span class="btn-tab"></span><span style="margin-left:18px">SEND MESSAGE &nbsp;›</span></div>

  <!-- footer -->
  <footer class="site-footer">
    <div class="foot-brand">
      <div class="foot-mark"></div>
      <div class="foot-name">PanelBrite</div>
      <div class="socials"><span></span><span></span><span></span><span></span><span></span></div>
    </div>
    <div class="foot-col" style="left:385px">
      <h4>NAVIGATION</h4>
      <ul><li>Home</li><li>Solar Cleaning</li><li>Gutter Cleaning</li><li>Resellers Portal</li><li>Customer portal</li><li>Contact Us</li></ul>
    </div>
    <div class="foot-col" style="left:586px">
      <h4>CONTACT US</h4>
      <ul>
        <li><svg width="12" height="12" viewBox="0 0 18 18" fill="#fff"><path d="M4 1l3 4-2 2c1 2 4 5 6 6l2-2 4 3-2 3C8 17 1 10 1 3z"/></svg>Sydney – 02 7391 5084</li>
        <li><svg width="12" height="12" viewBox="0 0 18 18" fill="#fff"><path d="M4 1l3 4-2 2c1 2 4 5 6 6l2-2 4 3-2 3C8 17 1 10 1 3z"/></svg>Southern Highlands – 02 4863 1507</li>
        <li><svg width="12" height="12" viewBox="0 0 18 18" fill="#fff"><path d="M4 1l3 4-2 2c1 2 4 5 6 6l2-2 4 3-2 3C8 17 1 10 1 3z"/></svg>Goulburn – 02 4863 1507</li>
        <li><svg width="12" height="12" viewBox="0 0 18 18" fill="#fff"><path d="M4 1l3 4-2 2c1 2 4 5 6 6l2-2 4 3-2 3C8 17 1 10 1 3z"/></svg>Canberra – 02 6178 3045</li>
        <li><svg width="12" height="12" viewBox="0 0 18 18" fill="#fff"><path d="M4 1l3 4-2 2c1 2 4 5 6 6l2-2 4 3-2 3C8 17 1 10 1 3z"/></svg>Wollongong – 02 4239 7615</li>
      </ul>
    </div>
    <div class="foot-col" style="left:882px">
      <h4>GET IN TOUCH</h4>
      <ul>
        <li><svg width="15" height="11" viewBox="0 0 20 14" fill="none" stroke="#fff" stroke-width="2"><rect x="1" y="1" width="18" height="12"/><path d="M1 1l9 7 9-7"/></svg>sales@panelbrite.com.au</li>
        <li style="align-items:flex-start;margin-top:18px"><svg width="14" height="18" viewBox="0 0 14 18" fill="#fff"><path d="M7 0C3 0 0 3 0 7c0 5 7 11 7 11s7-6 7-11c0-4-3-7-7-7zm0 10a3 3 0 110-6 3 3 0 010 6z"/></svg><span>Head Office -<br>Ferndell NSW 2583<br>ABN: 48762093115</span></li>
      </ul>
    </div>
  </footer>
  <div class="footer-bar">Copyright © 2025 PanelBrite. All Right Reserved</div>

</div>
</body>
</html>
```